A Book Cover For a Book Called "Lantern"

Attached are two files for the ISBN bar graph for the print version of the cover! Same image, just two different formats.
Updates

Target Market(s)

young adult female, parents

Colors

```html
<!DOCTYPE html>
<html lang="en">
<head>
<meta charset="utf-8">
<title>Lantern — A Memoir, cover</title>
<link rel="stylesheet" href="https://fonts.googleapis.com/css2?family=Bebas+Neue&family=Oswald:wght@700&family=Roboto+Condensed:wght@500&display=swap">
<style>
  :root {
    --backdrop: #e4e4e2;
    --cover-black: #050505;
    --title-white: #ffffff;
    --lavender: #c8a6f0;
    --band-text: #111111;
    --photo-light: #d9d9d9;
    --photo-mid: #8d8d8d;
    --photo-dark: #2a2a2a;
  }
  html, body {
    margin: 0;
    padding: 0;
    width: 1158px;
    height: 1200px;
    overflow: hidden;
    background: var(--backdrop);
  }
  .book-cover {
    position: absolute;
    left: 229px;
    top: 45px;
    width: 700px;
    height: 1110px;
    background: var(--cover-black);
    overflow: hidden;
  }
  .subtitle-band {
    position: absolute;
    left: 0;
    right: 0;
    top: 800px;
    height: 66px;
    background: var(--lavender);
  }
  .subtitle-band__text {
    position: absolute;
    left: 126px;
    top: 50%;
    transform: translateY(-50%);
    margin: 0;
    font-family: "Oswald", "Arial Narrow", sans-serif;
    font-weight: 700;
    font-size: 50px;
    line-height: 1;
    letter-spacing: 1px;
    color: var(--band-text);
  }
  .cover-photo {
    position: absolute;
    left: 430px;
    top: 70px;
    width: 220px;
    height: 1040px;
    border-radius: 90px 110px 0 0;
    background: linear-gradient(180deg, var(--photo-light) 0%, var(--photo-mid) 45%, var(--photo-light) 70%, var(--photo-dark) 100%);
  }
  .cover-title {
    position: absolute;
    inset: 0;
    width: 700px;
    height: 1110px;
  }
  .cover-title__line {
    font-family: "Bebas Neue", "Oswald", sans-serif;
    font-size: 488px;
    fill: var(--title-white);
  }
  .cover-byline {
    position: absolute;
    left: 126px;
    top: 985px;
    margin: 0;
    font-family: "Roboto Condensed", "Arial Narrow", sans-serif;
    font-weight: 500;
    font-size: 27px;
    color: var(--lavender);
  }
</style>
</head>
<body>
  <main class="book-cover">
    <div class="subtitle-band">
      <p class="subtitle-band__text">A MEMOIR</p>
    </div>
    <div class="cover-photo" role="img" aria-label="Black and white photo of a satin pointe shoe on a dancer's foot, held by a hand at the ankle"></div>
    <svg class="cover-title" viewBox="0 0 700 1110" aria-label="Lantern">
      <text class="cover-title__line" x="126" y="390" textLength="300" lengthAdjust="spacingAndGlyphs">LAN</text>
      <text class="cover-title__line" x="126" y="745" textLength="300" lengthAdjust="spacingAndGlyphs">TERN</text>
    </svg>
    <p class="cover-byline">by Marin Hale with Tessa Locke</p>
  </main>
</body>
</html>
```